Business card design to suit our website

Need a nice looking business card for our business based off images from our Website and provided images. The business card will require 2 different names (for the 2 owners). The business card should include images from our website, facebook (larkvale coil starter pack) or the pictures provided. it should also contain all contact information.
Our website is www.larkvalecoilworks.com.au
Please dont use image from top bar of website. If images are used please use the ones of our product under the buy it now tab
Updates

Need extra days to review

Target Market(s)

Automotive

Industry/Entity Type

Automotive Part

Contact Information for Business Card

Business Name. contact details including names phone number email. logo
2 business cards needed with 2 different persons names and phone number.

Colors

Designer to choose colors to be used in the design.

Requirements
Must have
• whatever looks best

```html
<!DOCTYPE html>
<html lang="en">
<head>
<meta charset="utf-8">
<title>Larkvale Coil Works – Business Card</title>
<link rel="stylesheet" href="https://fonts.googleapis.com/css2?family=Roboto:wght@400;500;700&family=Roboto+Condensed:wght@500;700&display=swap">
<style>
  :root {
    --backdrop: #2a2a2a;
    --card: #f2f2f2;
    --brand-red: #c0202b;
    --ink: #111111;
    --muted: #4a4a4a;
    --frame: #7a7a7a;
    --photo-dark: #3b3a38;
    --photo-mid: #6f6a62;
    --photo-light: #a7a39b;
  }
  * { margin: 0; padding: 0; box-sizing: border-box; }
  html, body { width: 1200px; height: 960px; overflow: hidden; }
  body {
    background: var(--backdrop);
    position: relative;
    font-family: "Roboto", Arial, sans-serif;
  }
  .card {
    position: absolute;
    width: 600px;
    height: 342px;
    background: var(--card);
  }
  .card--front { left: 322px; top: 108px; }
  .card--back { left: 320px; top: 493px; }

  .brand-name {
    position: absolute;
    left: 0; right: 0;
    text-align: center;
    font-family: "Roboto", Arial, sans-serif;
    font-weight: 700;
    color: var(--brand-red);
  }
  .card--front .brand-name { top: 100px; font-size: 30px; letter-spacing: 1px; }
  .product-line {
    position: absolute;
    left: 0; right: 0;
    top: 146px;
    text-align: center;
    font-size: 15px;
    font-weight: 500;
    color: var(--muted);
  }
  .holder {
    position: absolute;
    left: 0; right: 0;
    top: 174px;
    text-align: center;
    white-space: nowrap;
  }
  .holder__name {
    font-family: "Roboto Condensed", Arial, sans-serif;
    font-weight: 700;
    font-size: 24px;
    color: var(--brand-red);
  }
  .holder__role {
    font-family: "Roboto", Arial, sans-serif;
    font-weight: 500;
    font-size: 16px;
    color: var(--ink);
  }
  .contact {
    position: absolute;
    left: 0; right: 0;
    top: 208px;
    text-align: center;
    font-size: 15px;
    line-height: 19px;
    color: var(--muted);
  }

  .band {
    position: absolute;
    left: 0; right: 0;
    background: var(--brand-red);
  }
  .band--upper { top: 44px; height: 23px; }
  .band--lower { top: 77px; height: 25px; }
  .card--back .brand-name {
    top: 10px;
    font-size: 34px;
    line-height: 58px;
    color: #ffffff;
  }
  .card--back .brand-name span {
    background: var(--brand-red);
    padding: 0 14px;
  }
  .card--back .product-band-text {
    position: absolute;
    left: 0; right: 0;
    top: 77px;
    line-height: 25px;
    text-align: center;
    font-size: 19px;
    font-weight: 700;
    color: #ffffff;
  }
  .photo-strip {
    position: absolute;
    left: 24px;
    top: 127px;
    width: 547px;
    height: 190px;
    border: 3px solid var(--frame);
    border-radius: 11px;
    overflow: hidden;
    display: flex;
  }
  .photo-strip__panel {
    flex: 1;
    border-right: 3px solid #ffffff;
  }
  .photo-strip__panel:last-child { border-right: none; }
  .photo-strip__panel--a { background: linear-gradient(160deg, var(--photo-mid), var(--photo-dark)); }
  .photo-strip__panel--b { background: linear-gradient(200deg, var(--photo-dark), var(--photo-light)); }
  .photo-strip__panel--c { background: linear-gradient(180deg, #8a7f6c, #3d4f7a 55%, var(--photo-light)); }
  .photo-strip__panel--d { background: linear-gradient(150deg, #4c6b58, var(--photo-light) 60%, var(--photo-mid)); }
</style>
</head>
<body>
  <section class="card card--front" aria-label="Business card front">
    <div class="brand-name">Larkvale</div>
    <div class="product-line">Coil Starter Pack</div>
    <div class="holder">
      <span class="holder__name">Daniel Marsh -</span>
      <span class="holder__role">CEO/Founder</span>
    </div>
    <div class="contact">
      1300 482 716 | daniel@larkvalecoilworks.com.au<br>
      www.larkvalecoilworks.com.au
    </div>
  </section>

  <section class="card card--back" aria-label="Business card back">
    <div class="band band--upper"></div>
    <div class="band band--lower"></div>
    <div class="brand-name"><span>Larkvale</span></div>
    <div class="product-band-text">Coil Starter Pack</div>
    <div class="photo-strip">
      <div class="photo-strip__panel photo-strip__panel--a" role="img" aria-label="Car dashboard with illuminated ignition barrel"></div>
      <div class="photo-strip__panel photo-strip__panel--b" role="img" aria-label="Hands fitting the ignition switch housing"></div>
      <div class="photo-strip__panel photo-strip__panel--c" role="img" aria-label="Ignition lock part held in a blue bench vice"></div>
      <div class="photo-strip__panel photo-strip__panel--d" role="img" aria-label="Steering column with switch assembly installed"></div>
    </div>
  </section>
</body>
</html>
```